Psychology text book for statistics needs front cover

We need a logo/picture that will be the front cover of our book.

Our book is on person-specific data analysis. Such as: predicting when someone might binge drink, understanding personal processes (e.g., emotional processes; brain processes), or quantifying what depression means for a given individual.

So, something that merges the concept of people as individuals with their own processes (or life path) with statistics would be great.

Target Market(s)

Higher education

Logo Text

Mapping of Tidal Echo Patterns (optional)

Logo styles of interest
Pictorial/Combination Logo
Abstract Logo
Font styles to use
Sans Serif

Requirements
Must have
• The title of the book is:
Mapping of Tidal Echo Patterns: Lantern Methods for Quiet Signal Review

It would be fine to just include the first part - Mapping of Tidal Echo Patterns
Nice to have
• For inspiration: perhaps something that has a clear image of an individual in a crowd where everyone else is blurry. Or on a path. If you could figure out how to meld this together with some image representing data across time (such as lines on a plot see examples), that would be great.

```html
<!DOCTYPE html>
<html lang="en">
<head>
<meta charset="utf-8">
<title>Mapping of Tidal Echo Patterns — Cover</title>
<link rel="stylesheet" href="https://fonts.googleapis.com/css2?family=Cinzel:wght@400&family=Barlow+Condensed:ital,wght@1,600&display=swap">
<style>
  :root {
    --stage: #c9d1d1;
    --cover-top: #0b1226;
    --cover-bottom: #03050c;
    --ink: #f2f0ec;
    --ink-soft: #d9dbe0;
    --art-warm: #d9875a;
    --art-violet: #7a3f9e;
    --art-blue: #2f7fd6;
  }
  * { box-sizing: border-box; margin: 0; padding: 0; }
  html, body { width: 1200px; height: 800px; overflow: hidden; }
  body {
    background: var(--stage);
    display: flex;
    align-items: center;
    justify-content: center;
  }
  .cover {
    position: relative;
    width: 508px;
    height: 760px;
    background: linear-gradient(180deg, var(--cover-top) 0%, var(--cover-bottom) 100%);
    overflow: hidden;
  }
  .series-line {
    position: absolute;
    top: 50px;
    left: 0;
    right: 0;
    text-align: center;
    font-family: "Barlow Condensed", sans-serif;
    font-style: italic;
    font-weight: 600;
    font-size: 17px;
    letter-spacing: 1.6px;
    color: var(--ink-soft);
    text-transform: uppercase;
  }
  .title {
    position: absolute;
    top: 96px;
    left: 0;
    right: 0;
    text-align: center;
    font-family: "Cinzel", serif;
    font-weight: 400;
    color: var(--ink);
    line-height: 1;
  }
  .title-main {
    display: block;
    font-size: 78px;
    letter-spacing: 1px;
  }
  .title-mid {
    display: block;
    font-size: 40px;
    letter-spacing: 2px;
    margin: 4px 0 2px;
  }
  .title-last {
    display: block;
    font-size: 70px;
    letter-spacing: 0;
  }
  .cover-art {
    position: absolute;
    left: 16px;
    top: 292px;
    width: 470px;
    height: 360px;
    border-radius: 46% 50% 44% 52%;
    background:
      radial-gradient(ellipse 42% 40% at 52% 52%, var(--art-warm) 0%, rgba(217,135,90,0.6) 45%, transparent 75%),
      radial-gradient(ellipse 55% 45% at 50% 35%, rgba(47,127,214,0.55) 0%, transparent 70%),
      radial-gradient(ellipse 60% 55% at 50% 60%, rgba(122,63,158,0.5) 0%, transparent 75%);
  }
  .author {
    position: absolute;
    top: 690px;
    left: 0;
    right: 0;
    text-align: center;
    font-family: "Cinzel", serif;
    font-size: 23px;
    letter-spacing: 1px;
    color: var(--ink);
  }
</style>
</head>
<body>
  <main class="cover">
    <p class="series-line">Lantern Methods for Quiet Signal Review</p>
    <h1 class="title">
      <span class="title-main">Mapping</span>
      <span class="title-mid">of Tidal Echo</span>
      <span class="title-last">Patterns</span>
    </h1>
    <div class="cover-art" role="img" aria-label="Illustration of a glowing orange human brain wrapped in a blue and violet network of connected points and lines"></div>
    <p class="author">AUTHOR NAME</p>
  </main>
</body>
</html>
```